Webpage layout and company logo combination

We are trying to renovate an existing site to make it sharper and sophisticated in appearance. This is the existing site: http://www.brindlemorehomes.com/agents.html . The new presentation should be bright, sharp, sophisticated and should incorporate two additional menu tabs. The menu tabs will be revised as follows: Property Listings, Property Management, Advisory & Consulting, Local Info, R/E Tools, Our Team (please disregard Korean language characters, which will be installed after English version is completed, separately).

It Company

```html
<!DOCTYPE html>
<html lang="en">
<head>
<meta charset="utf-8">
<title>Brindlemore Homes</title>
<link href="https://fonts.googleapis.com/css2?family=Open+Sans:wght@400;600&family=Roboto:ital,wght@0,400;0,500;1,500&display=swap" rel="stylesheet">
<style>
:root{
  --blue:#1b67ad;
  --sky:#35a0dc;
  --nav-top:#2a86cc;
  --nav-bottom:#0f5b9f;
  --text:#555;
  --label:#1b67ad;
  --card:#f6f6f6;
  --card-line:#dcdcdc;
  --grey-btn:#6b6b6b;
  --footer:#343434;
  --footer-text:#bdbdbd;
}
*{margin:0;padding:0;box-sizing:border-box}
html,body{width:855px;height:1200px;overflow:hidden;background:#fff}
body{position:relative;font-family:'Open Sans',sans-serif;color:var(--text);font-size:9px}
.top-band{position:absolute;left:0;top:0;width:855px;height:154px;background:linear-gradient(#fff,#ececec)}
.brand{position:absolute;left:52px;top:70px;display:flex;align-items:center;gap:6px;font-family:'Roboto',sans-serif;font-weight:500;font-size:15px;color:var(--blue);letter-spacing:.3px}
.brand-mark{width:14px;height:14px;background:var(--blue)}
.utility{position:absolute;right:52px;top:13px;display:flex;align-items:center;gap:8px;font-size:9px;color:#666}
.phone{display:flex;align-items:center;gap:6px;font-family:'Roboto',sans-serif;font-size:13px;color:var(--blue);margin-right:6px}
.utility .sep{color:#aaa}
.utility .news{color:var(--blue)}
.lang{display:flex;align-items:center;gap:4px;border:1px solid #ccc;background:#fff;padding:2px 5px;font-size:8px;color:#333}
.flag{width:13px;height:9px;background:#2a4a8f}
.calc{position:absolute;left:443px;top:49px;width:160px;height:35px;background:var(--sky);display:flex;align-items:center;color:#fff;font-family:'Roboto',sans-serif;font-weight:500;font-size:12px}
.calc-icon{width:40px;height:35px;background:#fff;border:2px solid var(--sky);display:flex;align-items:center;justify-content:center;margin-right:7px}
.search{position:absolute;left:611px;top:53px;width:192px;height:25px;display:flex}
.search-field{flex:1;border:1px solid #ccc;background:#fff;font-size:8px;font-style:italic;color:#999;padding:6px 7px}
.search-btn{width:33px;background:#555;display:flex;align-items:center;justify-content:center}
.nav{position:absolute;left:52px;top:99px;width:751px;height:30px;background:linear-gradient(var(--nav-top),var(--nav-bottom));display:flex;justify-content:space-between;align-items:center;padding:0 11px;font-family:'Roboto',sans-serif;font-size:8.6px;color:#fff;letter-spacing:.3px}
.hero{position:absolute;left:52px;top:129px;width:751px;height:269px;background:linear-gradient(100deg,#5f7f4a 0%,#d9d6c8 30%,#c7cccc 45%,#3f78b4 65%,#6f9ccc 100%)}
.hero-caption{position:absolute;left:401px;top:77px;width:350px;height:116px;background:rgba(20,38,60,.85);padding:9px 22px}
.hero-title{font-family:'Roboto',sans-serif;font-style:italic;font-weight:500;font-size:22px;color:var(--sky)}
.hero-text{font-size:12px;color:#fff;line-height:16px;margin-top:3px}
.btn-find{display:inline-block;margin-top:10px;width:118px;height:24px;background:var(--sky);color:#fff;font-family:'Roboto',sans-serif;font-weight:500;font-size:11.5px;text-align:center;line-height:24px}
.dots{position:absolute;left:345px;top:241px;display:flex;gap:5px}
.dots span{width:11px;height:11px;border-radius:50%;background:#fff}
.dots span.on{background:var(--sky)}
.welcome-photo{position:absolute;left:52px;top:425px;width:193px;height:146px;border:3px solid #fff;box-shadow:0 0 0 1px #ddd;background:linear-gradient(#2f5f9c,#9ab7d6 65%,#6d7585)}
.welcome{position:absolute;left:268px;top:424px;width:535px}
h2{font-family:'Roboto',sans-serif;font-weight:400;font-size:17px;color:var(--blue);letter-spacing:.3px}
.welcome p{font-size:9.2px;line-height:16.4px;margin-top:5px}
.welcome h2{margin-bottom:4px}
.divider{position:absolute;left:52px;top:592px;width:751px;height:1px;background:#ccc}
.listings{position:absolute;left:52px;top:611px;width:493px}
.agents{position:absolute;left:566px;top:611px;width:237px}
.listings h2,.agents h2{margin-bottom:10px}
.property{position:relative;height:141px;background:var(--card);border:1px solid var(--card-line);margin-bottom:9px}
.property-photo{position:absolute;left:14px;top:12px;width:170px;height:115px;border:2px solid #fff;box-shadow:0 0 0 1px #ccc}
.p1{background:linear-gradient(#cfd9e3,#7b8a63 55%,#56703b)}
.p2{background:linear-gradient(#dfe3e6,#9a5040 55%,#8d8b7c)}
.p3{background:linear-gradient(#c9d3dc,#8b5a3f 45%,#6d6a63)}
.facts{position:absolute;left:201px;top:12px;width:280px;display:grid;grid-template-columns:71px 1fr;row-gap:2px;font-size:8.4px;line-height:14px}
.facts dt{font-family:'Roboto',sans-serif;font-size:10px;color:var(--label)}
.facts dd.town{font-family:'Roboto',sans-serif;font-weight:500;font-size:10px;color:var(--blue)}
.actions{position:absolute;left:201px;top:101px;display:flex;gap:4px}
.price{width:93px;height:27px;background:var(--sky);color:#fff;font-family:'Roboto',sans-serif;font-weight:500;font-size:12.5px;text-align:center;line-height:27px}
.more{width:93px;height:27px;background:var(--grey-btn);color:#fff;font-size:9px;text-align:center;line-height:27px}
.agent{position:relative;height:104px;background:linear-gradient(#fff,#f0f0f0);border:1px solid var(--card-line);margin-bottom:8px}
.agent-photo{position:absolute;left:12px;top:12px;width:65px;height:65px;border:2px solid #fff;box-shadow:0 0 0 1px #ccc;background:linear-gradient(#b9b3aa,#59504a)}
.agent-info{position:absolute;left:89px;top:10px;font-size:8.4px;line-height:13px}
.agent-name{font-family:'Roboto',sans-serif;font-weight:500;font-size:10px;color:var(--blue)}
.agent-role{font-size:8.4px;color:var(--sky);margin-bottom:2px}
.agent-info dl{display:grid;grid-template-columns:47px 1fr}
.agent-info dt{color:var(--label)}
.footer{position:absolute;left:0;top:1101px;width:855px;height:99px;background:var(--footer);color:var(--footer-text);font-size:8px}
.footer-links{position:absolute;left:52px;top:17px;display:flex;gap:6px}
.footer-links .sep{color:#888}
.copyright{position:absolute;left:52px;top:54px;line-height:14px}
.copyright .name{color:var(--sky)}
.connect{position:absolute;left:713px;top:17px;font-family:'Roboto',sans-serif;font-size:11px;color:var(--sky)}
.social{position:absolute;left:714px;top:41px;display:flex;gap:4px}
.social span{width:19px;height:19px;border-radius:2px}
</style>
</head>
<body>
<div class="top-band"></div>

<div class="brand"><span class="brand-mark"></span>BRINDLEMORE HOMES</div>

<div class="utility">
  <span class="phone">
    <svg width="13" height="13" viewBox="0 0 13 13"><rect width="13" height="13" rx="2" fill="#1b67ad"/><path d="M4 3l1.5 0 .7 2-1 .8c.5 1 1.2 1.7 2.2 2.2l.8-1 2 .7V9.5c0 .4-.4.7-.8.7C6 10 3 7 2.8 3.8 2.8 3.4 3.2 3 3.6 3z" fill="#fff"/></svg>
    (555) 410-2730
  </span>
  <span>Log in</span><span class="sep">|</span><span>Register</span><span class="sep">|</span><span class="news">Newsletter Signup</span>
  <span class="lang"><span class="flag"></span>English ▾</span>
</div>

<div class="calc">
  <span class="calc-icon">
    <svg width="20" height="22" viewBox="0 0 20 22"><rect x="1" y="1" width="15" height="20" rx="1" fill="none" stroke="#333" stroke-width="1.6"/><rect x="4" y="4" width="9" height="4" fill="#333"/><g fill="#333"><rect x="4" y="11" width="2" height="2"/><rect x="8" y="11" width="2" height="2"/><rect x="4" y="15" width="2" height="2"/><rect x="8" y="15" width="2" height="2"/></g><text x="12" y="20" font-size="9" font-family="Roboto,sans-serif" font-weight="500" fill="#333">%</text></svg>
  </span>
  Mortgage Calculator
</div>

<div class="search">
  <div class="search-field">Search Keywords...</div>
  <div class="search-btn"><svg width="16" height="16" viewBox="0 0 16 16"><circle cx="10" cy="6" r="4" fill="none" stroke="#fff" stroke-width="2"/><path d="M7 9l-5 5" stroke="#fff" stroke-width="3" stroke-linecap="round"/></svg></div>
</div>

<nav class="nav">
  <span>HOME</span><span>PROPERTY LISTINGS</span><span>PROPERTY MANAGEMENT</span><span>ADVISORY &amp; CONSULTING</span><span>LOCAL INFO</span><span>R/E TOOLS</span><span>OUR TEAM</span><span>CONTACT US</span>
</nav>

<section class="hero" role="img" aria-label="Large white two-storey family house with lawn under a blue sky">
  <div class="hero-caption">
    <div class="hero-title">Find the House of Your Dream</div>
    <div class="hero-text">Aenean lacinia sodales eros, sit amet molestie enim consectetur eget.</div>
    <div class="btn-find">Find Property</div>
  </div>
  <div class="dots"><span class="on"></span><span></span><span></span><span></span></div>
</section>

<div class="welcome-photo" role="img" aria-label="Business handshake above a city skyline"></div>
<section class="welcome">
  <h2>WELCOME TO BRINDLEMORE HOMES</h2>
  <p>Aliquam molestie, mi et imperdiet euismod, dui purus auctor tellus, et interdum lacus lectus et ante. Sed accumsan sollicitudin sapien, sit amet adipiscing turpis gravida ac. In congue, neque ac lobortis volutpat, libero mauris varius mi, vitae suscipit ipsum ligula vitae risus. Duis aliquam nibh a dui iaculis viverra id a velit. Vivamus egestas risus in magna varius commodo. Sed semper viverra egestas. Etiam pretium porttitor lectus, vel ornare neque porta volutpat.</p>
  <p>Aenean a nibh eget turpis vehicula tempus ac sed massa. Vestibulum dolor nulla, ultrices ac tincidunt sed, laoreet non est. Suspendisse lobortis turpis in odio blandit ac interdum lorem euismod. Etiam risus massa, vulputate eu pellentesque et, consectetur a neque.</p>
</section>

<div class="divider"></div>

<section class="listings">
  <h2>PROPERTY LISTING</h2>
  <article class="property">
    <div class="property-photo p1" role="img" aria-label="Townhouse complex beside a landscaped park"></div>
    <dl class="facts">
      <dt>Location:</dt><dd class="town">Larkhaven, NJ</dd>
      <dt>Description:</dt><dd>Willow Bend. Perfect blend of design, privacy and standard of living. River front community. Ashford model Hardwood ...</dd>
      <dt>MLS ID:</dt><dd>1048372</dd>
    </dl>
    <div class="actions"><span class="price">$625,000</span><span class="more">More Details</span></div>
  </article>
  <article class="property">
    <div class="property-photo p2" role="img" aria-label="Red brick two-family house on a street corner"></div>
    <dl class="facts">
      <dt>Location:</dt><dd class="town">Larkhaven, NJ</dd>
      <dt>Description:</dt><dd>Willow Bend. Perfect blend of design, privacy and standard of living. River front community. Ashford model Hardwood ...</dd>
      <dt>MLS ID:</dt><dd>1048372</dd>
    </dl>
    <div class="actions"><span class="price">$625,000</span><span class="more">More Details</span></div>
  </article>
  <article class="property">
    <div class="property-photo p3" role="img" aria-label="New brick duplex with arched windows"></div>
    <dl class="facts">
      <dt>Location:</dt><dd class="town">Larkhaven, NJ</dd>
      <dt>Description:</dt><dd>Willow Bend. Perfect blend of design, privacy and standard of living. River front community. Ashford model Hardwood ...</dd>
      <dt>MLS ID:</dt><dd>1048372</dd>
    </dl>
    <div class="actions"><span class="price">$625,000</span><span class="more">More Details</span></div>
  </article>
</section>

<section class="agents">
  <h2>OUR AGENTS</h2>
  <article class="agent">
    <div class="agent-photo" role="img" aria-label="Portrait of the broker"></div>
    <div class="agent-info">
      <div class="agent-name">Harold Jun</div><div class="agent-role">Broker/Owner</div>
      <dl><dt>Direct:</dt><dd>555-302-4410</dd><dt>Office:</dt><dd>555-410-2730</dd><dt>Cell:</dt><dd>555-618-3390</dd><dt>Email:</dt><dd>hjun22@mailbox.net</dd></dl>
    </div>
  </article>
  <article class="agent">
    <div class="agent-photo" role="img" aria-label="Portrait of a sales agent"></div>
    <div class="agent-info">
      <div class="agent-name">Jason Ko</div><div class="agent-role">Sales Agent</div>
      <dl><dt>Direct:</dt><dd>555-302-4410</dd><dt>Office:</dt><dd>555-410-2730</dd><dt>Cell:</dt><dd>555-618-3390</dd><dt>Email:</dt><dd>jko22@mailbox.net</dd></dl>
    </div>
  </article>
  <article class="agent">
    <div class="agent-photo" role="img" aria-label="Portrait of a sales agent"></div>
    <div class="agent-info">
      <div class="agent-name">Sophie Lin</div><div class="agent-role">Sales Agent</div>
      <dl><dt>Direct:</dt><dd>555-302-4410</dd><dt>Office:</dt><dd>555-410-2730</dd><dt>Cell:</dt><dd>555-618-3390</dd><dt>Email:</dt><dd>hjun22@mailbox.net</dd></dl>
    </div>
  </article>
  <article class="agent">
    <div class="agent-photo" role="img" aria-label="Portrait of a sales agent"></div>
    <div class="agent-info">
      <div class="agent-name">Kevin Park</div><div class="agent-role">Sales Agent</div>
      <dl><dt>Direct:</dt><dd>555-302-4410</dd><dt>Office:</dt><dd>555-410-2730</dd><dt>Cell:</dt><dd>555-618-3390</dd><dt>Email:</dt><dd>hjun22@mailbox.net</dd></dl>
    </div>
  </article>
</section>

<footer class="footer">
  <div class="footer-links">
    <span>Home</span><span class="sep">/</span><span>Property Listings</span><span class="sep">/</span><span>Property Management</span><span class="sep">/</span><span>Advisory &amp; Consulting</span><span class="sep">/</span><span>Local Info</span><span class="sep">/</span><span>R/E Tools</span><span class="sep">/</span><span>Our Team</span><span class="sep">/</span><span>Contact us</span>
  </div>
  <div class="copyright">Copyright © 2014. <span class="name">Brindlemore Homes</span>. All Right Reserved<br>Privacy Policy &nbsp;|&nbsp; Term of Services</div>
  <div class="connect">Connect Us</div>
  <div class="social">
    <span style="background:#3b5a9a"></span><span style="background:#3fb3e2"></span><span style="background:#e8832a"></span><span style="background:#c4302b"></span>
  </div>
</footer>
</body>
</html>
```